Video Sharing Site

UPDATE 2: Thanks to everyone who has submitted so far. I have decided to include 2nd and 3rd prizes are well, and I believe with a robust price. If you chose to participate, I will be working with the 2nd and 3rd prize winners also to use your selected designs to complete the rest of the webpages as specified in the brief.

-

UPDATE 1: The key is attractive, SOPHISTICATED yet roomy.

You are free to use any software package you like ie. Joomla, Drupal, Wordpress etc. We just need access to the HTML/CSS.

-

Hello everyone.

We require the HTML/CSS for a video sharing website. Our website is called ClipHarborly.com. Think of a unique logo. However this is not the main focus. I will try to give you as much info about the website design as I can:

# Home page:
- with categories in sidebar
- video listings eg. popular, most viewed, etc.
- perhaps make promoted videos stand out

# simple login page

# User Profile page
- user details
- user uploaded videos
- profile comments

# User Profile Edit page

# User Profile Inbox page
- mock messages

# Search page
- list of videos that match search
- number of results
- pagination
- etc.

# Video page
- page where we are watching a video
- related videos
- video comments
- video description
- ratings (thumbs up/down)
- views
- tags
- etc.

# Video Categories page
- list of a few categories eg. newest, most viewed, highest rated, etc.
- with 10-15 videos under each

# Video Upload page with form

# About Us
- with subcategories in sidebar (different design to video categories in home page sidebar)

# Contact Us

# Header
- as any website an attractive search bar should accompany the header
- quick shortlinks to logged-in user eg. (5) comments, (3) inbox, logout, etc.

# Footer
- should be thick so that it can accommodate links to more specific (mock) web pages.

# General
- please be sure to include advertising
- Don't be afraid to use bold colors.
- I will not be selecting designs that are overly dark
- be sure that any page where video thumbnails are shown are accompanied by video rating, number of views and author.
- think about loading times as well. Avoid the use of large graphics where possible.

########### HINT ##########
The first two designs that I pick will be two different types:
- colorful
- quite conservative. Plenty of white with light greys
###########################

Thanks everybody who submits!

2nd and 3rd prized now included!

Just to keep you all updated. I have made a few changes to the brief. Mostly just to make it easier for you to gauge what I'm after.

I have received enough designs with blue in it. Please submit designs where blue is not a main color. Thank you all!

Industry/Entity Type

Software

Requirements
Must have
• A sophisticated layout. It must look like a professional video sharing website.

```html
<!DOCTYPE html>
<html lang="en">
<head>
<meta charset="utf-8">
<title>ClipHarborly.com – Home</title>
<link rel="stylesheet" href="https://fonts.googleapis.com/css2?family=Noto+Sans:wght@400;700&display=swap">
<style>
:root{
  --lime:#b3cb12;
  --sub-bar:#f1f1f1;
  --ink:#222;
  --muted:#777;
  --cyan:#2bb8e0;
  --blue:#1e98c6;
  --blue-dark:#137fab;
  --blue-light:#3fb3dc;
  --banner:#0b1013;
  --page:#efeeee;
  --panel:#f3f2f2;
  --panel-line:#dcdcdc;
  --footer:#0b5a78;
  --footer-dark:#074a64;
  --btn-green:#6fb316;
  --star:#f0b400;
}
*{box-sizing:border-box;margin:0;padding:0}
html,body{width:805px;height:1200px;overflow:hidden}
body{position:relative;background:#fff;font-family:"Noto Sans",Arial,sans-serif;color:var(--ink);font-size:9px}
.abs{position:absolute}
a{color:inherit;text-decoration:none}

/* top bars */
.top-bar{left:0;top:0;width:805px;height:18px;background:var(--lime);font-size:10px;color:#2a3300}
.top-bar .nav-main{position:absolute;left:455px;top:2px}
.top-bar .nav-account{position:absolute;left:664px;top:2px}
.sep{margin:0 7px}
.user-bar{left:0;top:18px;width:805px;height:19px;background:var(--sub-bar);font-size:9px;color:#888;text-align:right;padding:3px 25px 0 0}

/* header */
.logo{left:22px;top:52px;display:flex;align-items:center;gap:8px}
.logo-mark{width:56px;height:56px;background:#1a1a1a;border-radius:6px}
.logo-name{font-size:31px;color:#4b9bc8;font-weight:400;letter-spacing:-.5px}
.search{left:420px;top:68px;width:361px;height:28px;border:1px solid #ddd;border-radius:14px;background:#fff;overflow:hidden}
.search span{position:absolute;left:14px;top:7px;color:#bbb;font-size:9px}
.search .go{position:absolute;right:0;top:0;width:34px;height:28px;background:#e8ebd8;border-left:1px solid #ddd}

/* banner */
.banner{left:0;top:138px;width:805px;height:258px;background:var(--banner)}
.banner-frame{left:24px;top:12px;width:756px;height:234px;border:1px solid #666}
.banner-media{left:3px;top:3px;width:403px;height:227px;background:linear-gradient(120deg,#3a2a26,#7a1c22 45%,#2d1e1c)}
.banner-title{left:424px;top:10px;font-size:20px;color:var(--cyan);font-weight:400}
.banner-sub{left:426px;top:36px;font-size:14px;color:#c9d800}
.banner-text{left:426px;top:64px;width:310px;font-size:10.5px;line-height:12.5px;color:#eee}
.btn-watch{left:427px;top:122px;width:88px;height:20px;background:var(--btn-green);border-radius:3px;color:#fff;font-size:10.5px;padding:3px 0 0 8px}
.btn-watch i{position:absolute;right:5px;top:3px;width:14px;height:14px;border:1.5px solid #fff;border-radius:50%}
.dots{left:668px;top:222px;display:flex;gap:5px}
.dots span{width:12px;height:12px;border-radius:50%;background:#3ab5e6;border:1px solid #9fdcf5}
.dots span:first-child{background:#9ccc1a}

/* main area */
.main{left:0;top:396px;width:805px;height:564px;background:var(--page)}
.sidebar{left:20px;top:10px;width:143px;height:537px;background:linear-gradient(var(--blue),var(--blue-dark));border-radius:10px;border:2px solid #fff}
.sidebar h2{position:absolute;left:11px;top:8px;font-size:14.5px;font-weight:400;color:#fff}
.cat-list{position:absolute;left:12px;top:41px;width:123px;list-style:none}
.cat-list li{height:24px;color:#fff;font-size:10.5px;padding:4px 0 0 12px;border-bottom:1px solid #4cb0d8;background:var(--blue-light)}
.cat-list li.on{background:#5ec4e6}
.cat-list li.gap{margin-top:5px}
.sidebar .see{position:absolute;right:10px;bottom:8px;color:#fff;font-size:10.5px}

.panel{background:var(--panel);border:2px solid #fff;border-radius:10px;overflow:hidden}
.center{left:174px;top:10px;width:399px;height:538px}
.sec-title{position:absolute;font-size:12.5px;color:var(--blue);font-weight:400}
.btn-see{position:absolute;width:56px;height:16px;background:var(--btn-green);border-radius:2px;color:#fff;font-size:10px;padding:1px 0 0 14px}
.btn-see:before{content:"";position:absolute;left:6px;top:4px;border-left:5px solid #fff;border-top:4px solid transparent;border-bottom:4px solid transparent}
.thumb{position:absolute;border:2px solid #fff;box-shadow:0 0 0 1px #ddd}
.dur{position:absolute;right:0;top:0;background:#000;color:#fff;font-size:8.5px;padding:1px 4px}
.card-info{position:absolute;width:176px;line-height:12px}
.card-info b{font-size:9px;display:block}
.card-info .by{color:var(--muted);font-size:8px}
.stars{color:var(--star);font-size:9px}
.divider{position:absolute;left:12px;width:371px;height:1px;background:var(--panel-line)}
.spot-title{position:absolute;left:10px;top:404px;font-size:11px}
.spot-text{position:absolute;left:10px;top:424px;width:222px;font-size:9px;line-height:13.5px}
.spot-by{position:absolute;left:10px;top:496px;font-size:8.5px;font-weight:700}

.featured{left:580px;top:7px;width:202px;height:258px}
.trailers{left:580px;top:274px;width:202px;height:274px}
.feat-item{position:absolute;left:7px;width:190px;height:52px;border-bottom:1px solid var(--panel-line)}
.feat-item .thumb{left:2px;top:3px;width:92px;height:44px}
.feat-item p{position:absolute;left:100px;top:6px;width:88px;color:var(--blue);font-size:8.5px;line-height:11px}
.feat-item small{position:absolute;left:100px;top:30px;font-size:8px;color:#444;white-space:nowrap}
.trailers .thumb{left:12px;width:176px;height:60px}

/* footer */
.footer{left:0;top:960px;width:805px;height:240px;background:var(--footer)}
.footer-cap{left:18px;top:-1px;width:764px;height:30px;background:var(--footer-dark);border-radius:18px 18px 0 0}
.foot-h{position:absolute;color:#fff;font-size:12.5px;font-weight:400}
.quick{position:absolute;left:53px;top:52px;list-style:none}
.quick li{color:#3fc4f0;font-size:9.5px;height:18px}
.quick li:before{content:"•";color:#fff;margin-right:7px}
.field{position:absolute;left:272px;width:190px;height:20px;background:#fff;border-radius:7px;font-size:8.5px;padding:4px 10px;color:#333}
.news-text{position:absolute;left:273px;top:96px;width:218px;color:#3fc4f0;font-size:9.5px;line-height:13px}
.btn-sub{position:absolute;left:271px;top:165px;width:134px;height:26px;background:linear-gradient(#8fd6f4,#3fa9dc);border-radius:4px;color:#0b2c46;font-weight:700;font-size:11px;padding:5px 0 0 12px}
.btn-sub i{position:absolute;right:10px;top:4px;width:17px;height:17px;border:2px solid #fff;border-radius:50%}
.social{position:absolute;top:46px;width:44px;height:44px;border-radius:7px}
.contact{position:absolute;left:580px;color:#fff;font-size:12px;display:flex;align-items:center;gap:10px}
.copyright{left:0;top:1178px;width:805px;text-align:center;color:#fff;font-size:8px}
</style>
</head>
<body>

<header>
  <div class="abs top-bar">
    <nav class="nav-main"><a>Browse</a><span class="sep">|</span><a>Movies</a><span class="sep">|</span><a>Upload</a></nav>
    <nav class="nav-account"><a>Create Account</a><span class="sep">|</span><a>Sign In</a></nav>
  </div>
  <div class="abs user-bar">Welcome Mara Lindqvist<span class="sep">|</span>My Account<span class="sep">|</span>Inbox(4)<span class="sep">|</span>Comments(5)<span class="sep">|</span>Log Out</div>

  <div class="abs logo"><span class="logo-mark"></span><span class="logo-name">ClipHarborly.com</span></div>
  <div class="abs search"><span>Search videos</span>
    <div class="go"><svg width="34" height="28" viewBox="0 0 34 28"><circle cx="18" cy="12" r="4.5" fill="none" stroke="#333" stroke-width="1.8"/><line x1="15" y1="15.5" x2="11.5" y2="19" stroke="#333" stroke-width="2.2"/></svg></div>
  </div>
</header>

<section class="abs banner">
  <div class="abs banner-frame">
    <div class="abs banner-media" role="img" aria-label="Video still of a child singing into a studio microphone"></div>
    <h1 class="abs banner-title">Why This Lullaby Lullaby Di</h1>
    <div class="abs banner-sub">(The Kid Version)</div>
    <p class="abs banner-text">Lorem ipsum dolor sit amet, consectetur adipiscing elit. Cras auctor molestie suscipit. Nulla facilisi.Lorem ipsum dolor sit amet, consectetur adipiscing elit. Cras auctor molestie suscipit. Nulla facilisi.</p>
    <a class="abs btn-watch">Watch Now<i></i></a>
    <div class="abs dots"><span></span><span></span><span></span><span></span><span></span></div>
  </div>
</section>

<main class="abs main">
  <aside class="abs sidebar">
    <h2>Video Categories</h2>
    <ul class="cat-list">
      <li class="on">Trending</li><li>Popular</li><li>Music</li><li>Entertainment</li><li>Sports</li>
      <li class="gap">Film &amp; Animation</li><li>News &amp; Politics</li><li>Comedy</li><li>Scinece</li><li>Technonlogy</li>
      <li class="gap">Style</li><li>Pets</li><li>Autos</li><li>Travel</li>
      <li class="gap">How To</li><li>Animals</li><li>Vehicles</li><li>Events</li><li>PERSONAL</li>
    </ul>
    <a class="see">&#9656; See All</a>
  </aside>

  <section class="abs panel center">
    <h3 class="sec-title" style="left:12px;top:8px">Most Viewed Today</h3>
    <a class="btn-see" style="left:350px;top:8px">See All</a>
    <div class="thumb" style="left:14px;top:32px;width:180px;height:70px;background:linear-gradient(90deg,#6e9a55,#c9d6c0)" role="img" aria-label="Video thumbnail of a family blowing bubbles outdoors"><span class="dur">5.16</span></div>
    <div class="card-info" style="left:18px;top:108px"><b>Dil Ki Baat Ka Naam Kya Hai</b><span class="by">Teo Ramires</span><br>3067 plays | Added 09-12-2011<br><span class="stars">★★★★★</span></div>
    <div class="thumb" style="left:205px;top:32px;width:180px;height:70px;background:linear-gradient(90deg,#f2f2f2,#6d5a4a 50%,#f0f0f0)" role="img" aria-label="Video thumbnail of an action film scene"><span class="dur">5.16</span></div>
    <div class="card-info" style="left:209px;top:108px"><b>Dil Ki Baat Ka Naam Kya Hai</b><span class="by">Teo Ramires</span><br>3067 plays | Added 09-12-2011<br><span class="stars">★★★★★</span></div>
    <div class="divider" style="top:182px"></div>

    <h3 class="sec-title" style="left:12px;top:198px">Popular</h3>
    <a class="btn-see" style="left:350px;top:198px">See All</a>
    <div class="thumb" style="left:14px;top:222px;width:180px;height:70px;background:linear-gradient(90deg,#2b3a66,#a34a2a 50%,#2a4c7a)" role="img" aria-label="Video thumbnail of an animated movie poster"><span class="dur">5.16</span></div>
    <div class="card-info" style="left:18px;top:298px"><b>Dil Ki Baat Ka Naam Kya Hai</b><span class="by">Teo Ramires</span><br>3067 plays | Added 09-12-2011<br><span class="stars">★★★★★</span></div>
    <div class="thumb" style="left:205px;top:222px;width:180px;height:70px;background:linear-gradient(#2e77b0,#4b8fc2 55%,#3a2f2a)" role="img" aria-label="Video thumbnail of a teen movie poster in front of school lockers"><span class="dur">5.16</span></div>
    <div class="card-info" style="left:209px;top:298px"><b>Dil Ki Baat Ka Naam Kya Hai</b><span class="by">Teo Ramires</span><br>3067 plays | Added 09-12-2011<br><span class="stars">★★★★★</span></div>
    <div class="divider" style="top:372px"></div>

    <h3 class="sec-title" style="left:10px;top:382px">Spotlight</h3>
    <a class="btn-see" style="left:350px;top:388px">See All</a>
    <div class="spot-title">Best Of Bollywood Hits: 2011</div>
    <p class="spot-text">From the beats of Chamka Chamki to the madness of Daud Daud Dil Dose - 2011 saw it all! Here's ClipHarborly's biggest Bollywood Hits for all music lovers out there! Lets sing and dance goodbye to a great year with clipharborly.com</p>
    <div class="spot-by">Presented By : Mara Lindqvist</div>
    <div class="thumb" style="left:238px;top:416px;width:147px;height:58px;background:linear-gradient(90deg,#c7dbe6,#7d9a6a 60%,#d8e4d0)" role="img" aria-label="Video thumbnail of a child among flowers"><span class="dur">5.16</span></div>
    <div class="card-info" style="left:242px;top:480px;width:150px"><b>Dil Ki Baat Ka Naam Kya Hai</b><span class="by">Teo Ramires</span><br>3067 plays | Added 09-12-2011<br><span class="stars">★★★★★</span></div>
  </section>

  <section class="abs panel featured">
    <h3 class="sec-title" style="left:12px;top:4px;font-size:13.5px">Featured Video</h3>
    <div class="feat-item" style="top:30px"><div class="thumb" style="background:linear-gradient(90deg,#e8c9cf,#9a4a4f)" role="img" aria-label="Featured video thumbnail"><span class="dur">3.19</span></div><p>Lorem ipsum dolor sit amet</p><small>By <b>Harbor News Desk</b></small></div>
    <div class="feat-item" style="top:84px"><div class="thumb" style="background:linear-gradient(90deg,#2a2f38,#6a5b52)" role="img" aria-label="Featured video thumbnail"><span class="dur">3.19</span></div><p>Lorem ipsum dolor sit amet</p><small>By <b>Harbor News Desk</b></small></div>
    <div class="feat-item" style="top:138px"><div class="thumb" style="background:linear-gradient(90deg,#4a5560,#9aa2aa)" role="img" aria-label="Featured video thumbnail"><span class="dur">3.19</span></div><p>Lorem ipsum dolor sit amet</p><small>By <b>Harbor News Desk</b></small></div>
    <div class="feat-item" style="top:192px;border:0"><div class="thumb" style="background:linear-gradient(90deg,#5a3a2e,#b8866a)" role="img" aria-label="Featured video thumbnail"><span class="dur">3.19</span></div><p>Lorem ipsum dolor sit amet</p><small>By <b>Harbor News Desk</b></small></div>
  </section>

  <section class="abs panel trailers">
    <h3 class="sec-title" style="left:12px;top:8px;font-size:14px">Latest Movie Official Trailers</h3>
    <div class="thumb" style="top:36px;background:linear-gradient(100deg,#1d2620,#5b6a5a 50%,#1f2520)" role="img" aria-label="Movie trailer thumbnail"><span class="dur">3.14</span></div>
    <div class="thumb" style="top:106px;background:linear-gradient(#0a2a3a,#1a6a8a 50%,#0a1a2a)" role="img" aria-label="Movie trailer thumbnail"><span class="dur">3.14</span></div>
    <div class="thumb" style="top:176px;background:linear-gradient(90deg,#2a2418,#a88a4a 50%,#3a3020)" role="img" aria-label="Movie trailer thumbnail"><span class="dur">3.14</span></div>
    <a class="btn-see" style="left:10px;top:244px">See All</a>
  </section>
</main>

<footer class="abs footer">
  <div class="abs footer-cap"></div>
  <h4 class="foot-h" style="left:53px;top:20px">Quick Links</h4>
  <ul class="quick"><li>Home</li><li>Browse</li><li>Movies</li><li>Upload</li><li>Profile</li><li>Contact Us</li></ul>

  <h4 class="foot-h" style="left:270px;top:22px">Subscribe Newsletters</h4>
  <div class="field" style="top:43px">Your name</div>
  <div class="field" style="top:71px">Your email id</div>
  <p class="news-text">Lorem ipsum dolor sit amet, consectetur adipiscing elit. Proin posuere ipsum sit amet urna bibendum iaculis. Etiam faucibus ultricies diam ac facilisis. Maecenas eleifend iaculis vulputate.</p>
  <a class="btn-sub">SUBSCRIBE NOW<i></i></a>

  <h4 class="foot-h" style="left:571px;top:22px">Follow Us</h4>
  <span class="social" style="left:573px;background:#2f5d9e" role="img" aria-label="Social network link"></span>
  <span class="social" style="left:630px;background:#3fb8e6" role="img" aria-label="Social network link"></span>
  <span class="social" style="left:688px;background:#e8702a" role="img" aria-label="Blog link"></span>

  <h4 class="foot-h" style="left:573px;top:104px">Contact Us</h4>
  <div class="contact" style="top:126px;font-size:14px">
    <svg width="20" height="22" viewBox="0 0 20 22"><path d="M4 2 L8 2 L9 7 L6.5 8.5 C7.5 11.5 9.5 13.5 12.5 14.5 L14 12 L19 13 L19 17 C19 18.5 17.5 20 16 20 C8.5 19.5 2.5 13.5 2 6 C2 4 3 2 4 2Z" fill="#e53030"/></svg>555 0142 786</div>
  <div class="contact" style="top:162px">
    <svg width="24" height="18" viewBox="0 0 24 18"><path d="M2 3 L22 3 L22 15 L2 15Z" fill="#2bbd9a"/><path d="M2 3 L12 10 L22 3" fill="none" stroke="#fff" stroke-width="1.4"/></svg>info@clipharborly.com</div>
</footer>
<div class="abs copyright">© 2011, All Rights Reserved, Privacy Policy<span class="sep">|</span>Terms &amp; Conditions<span class="sep">|</span>Sitemap</div>

</body>
</html>
```